BROCHURE OR FLYER PLEASE

We need a brochure design for our company TV Surfacing Contractors Limited. Our website is www.tvsurfacing-demo.co.nz. We have rented a 3m permanent booth at the dwelling plans hub in central Auckland. Their website is: www.dwellingplans-demo.co.nz
We need to design and provide a company brochure outlining who we are, and the types of services we provide. Half of our flooring business is dedicated to basically Polished Concrete/Concrete Grinding; and the other half to resin and other floor toppings. We are based in Auckland, NZ and will be marketing to existing and new home owners essentially in Auckland. We want to contain concise information on our services and present this in a professional but sheik style. Housing in NZ is expensive so our brochure needs to be up market and user friendly. Polished concrete is more expensive that carpet so I feel it is important to list the benefits etc. I will attach our website and information regarding our products. We would like a double sided brochure. Our company colours are blue/red/black. I have attached some photo's you are welcome to use. Please refer to our website for more information www.tvsurfacing-demo.co.nz. Thank you.

Target Market(s)

Home Owners

Industry/Entity Type

Marketing

Requirements
Must have
• Company logo and contact details.

```html
<!DOCTYPE html>
<html lang="en">
<head>
<meta charset="utf-8">
<title>TV Surfacing Contractors – Trifold Brochure</title>
<link href="https://fonts.googleapis.com/css2?family=Raleway:wght@300;400;600;800&family=Arimo:wght@400;700&display=swap" rel="stylesheet">
<style>
  :root {
    --stage: #e6e6e6;
    --blue: #6e9bd3;
    --blue-strip: #6a95cf;
    --red: #e8212b;
    --white: #ffffff;
    --ink: #111111;
    --photo-house-a: #c9d3dc;
    --photo-house-b: #2f6fc0;
    --photo-floor-a: #a7acb2;
    --photo-floor-b: #2c2c2e;
  }
  * { box-sizing: border-box; margin: 0; padding: 0; }
  html, body {
    width: 1200px; height: 800px; overflow: hidden;
    background: var(--stage);
    font-family: "Raleway", "Helvetica Neue", sans-serif;
  }
  .brochure {
    position: absolute; left: 210px; top: 110px;
    width: 780px; height: 580px;
    display: flex;
    box-shadow: 0 10px 30px rgba(0,0,0,.18);
  }
  .panel { width: 260px; height: 100%; position: relative; overflow: hidden; }

  /* Services panel */
  .panel--services { background: var(--blue); color: var(--white); padding: 34px 22px 0 24px; }
  .services__title { font-weight: 600; font-size: 9.5px; letter-spacing: .3px; text-transform: uppercase; margin-bottom: 14px; }
  .services__text { font-weight: 300; font-size: 9.5px; line-height: 1.45; margin-bottom: 12px; }
  .services__list { list-style: disc; padding-left: 14px; font-weight: 300; font-size: 9.5px; line-height: 1.45; margin-bottom: 14px; }
  .guarantee__title { font-weight: 300; font-size: 25px; line-height: 1.05; margin-bottom: 16px; }
  .guarantee__text { font-weight: 300; font-size: 9.5px; line-height: 1.5; margin-bottom: 18px; padding-left: 14px; }
  .cta { font-weight: 300; font-size: 13px; line-height: 1.45; padding-left: 14px; }

  /* About panel */
  .panel--about { background: var(--red); color: var(--white); padding: 34px 22px 0 22px; }
  .about__title { font-weight: 300; font-size: 25px; letter-spacing: 1px; margin-bottom: 10px; }
  .about__text { font-weight: 300; font-size: 9.5px; line-height: 1.5; margin-bottom: 14px; }
  .photo { display: block; }
  .about__photo {
    width: 216px; height: 150px;
    background: linear-gradient(180deg, var(--photo-house-a) 0%, #e9eef2 45%, var(--photo-house-b) 75%, #8a8f94 100%);
  }
  .brand-dot { display: block; margin: 30px auto 0; }
  .contact { text-align: center; font-size: 9.5px; line-height: 1.5; margin-top: 40px; font-weight: 400; font-style: normal; }
  .contact__name { font-weight: 600; text-transform: uppercase; }
  .contact__gap { height: 10px; }

  /* Cover panel */
  .panel--cover { background: var(--white); }
  .cover__strip { position: absolute; left: 0; right: 0; height: 12px; background: var(--blue-strip); }
  .cover__strip--top { top: 0; }
  .cover__strip--bottom { bottom: 0; }
  .logo { position: absolute; top: 36px; left: 20px; display: flex; align-items: center; gap: 10px; }
  .logo__mark { width: 22px; height: 22px; background: var(--red); }
  .logo__name { font-family: "Raleway", sans-serif; font-weight: 800; font-size: 17px; color: var(--ink); text-transform: uppercase; line-height: 1.05; }
  .tagline { position: absolute; top: 92px; left: 0; right: 0; text-align: center; font-family: "Arimo", Arial, sans-serif; font-size: 10.5px; line-height: 1.3; color: var(--ink); }
  .cover__photo {
    position: absolute; top: 136px; left: 0; right: 0; height: 380px;
    background: linear-gradient(160deg, var(--photo-floor-a) 0%, #d4d8dc 40%, #5c6064 70%, var(--photo-floor-b) 100%);
  }
  .cover__dot { position: absolute; left: 14px; bottom: 26px; }
</style>
</head>
<body>
  <main class="brochure">
    <section class="panel panel--services">
      <h2 class="services__title">Non-slip coatings and applications</h2>
      <p class="services__text">If you have an area in your property that requires a non-slip surface (such as a walk-ways, patio areas, garages, carports, bathrooms or pool surroundings etc), talk to us at TV Surfacing Contractors.</p>
      <p class="services__text">Our concrete systems and non-slip applications are ideal for a number of requirements, and will leave your concrete floors looking great!</p>
      <p class="services__text">Options may include:</p>
      <ul class="services__list">
        <li>Acid Washed Concrete and a specialised Sealant applied to protect and enhance the concrete</li>
        <li>Concrete Grinding and Sealant applied with specific non slip beads</li>
        <li>Velorin Flakestone – decorative Flooring with Flake Finish – Seamless, safe &amp; waterproof</li>
        <li>Velorin Gripcoat – non slip flooring</li>
      </ul>
      <h2 class="guarantee__title">Our guarantee<br>to you</h2>
      <p class="guarantee__text">Have complete peace of mind when dealing with us, as we provide a workmanship guarantee on all services.</p>
      <p class="cta">Arrange your free quote and consultation for concrete polishing, concrete preparation, non-slip coatings or resin floor toppings</p>
    </section>

    <section class="panel panel--about">
      <h2 class="about__title">ABOUT US</h2>
      <p class="about__text">Our New Zealand based, locally owned business has been successfully providing Auckland with reliable Flooring Services since 2001. With over 17 years experience as flooring specialists, our team are highly skilled when it comes to polished concrete floors, concrete block honing, concrete preparation, resin floor toppings and Non slip flooring options.</p>
      <div class="photo about__photo" role="img" aria-label="Photo of a modern two-storey white home with a blue swimming pool"></div>
      <svg class="brand-dot" width="22" height="22" viewBox="0 0 22 22" aria-hidden="true"><circle cx="11" cy="11" r="11" fill="#ffffff"/></svg>
      <address class="contact">
        <div class="contact__name">TV Surfacing Contractors</div>
        <div>PO BOX 1234</div>
        <div>AUCKLAND 0999</div>
        <div class="contact__gap"></div>
        <div>FREE PHONE: 0800 555 010</div>
        <div>EMAIL: info@tvsurfacing-demo.co.nz</div>
        <div>FAX: 09 555 0142</div>
        <div>WEBSITE: www.tvsurfacing-demo.co.nz</div>
      </address>
    </section>

    <section class="panel panel--cover">
      <div class="cover__strip cover__strip--top"></div>
      <div class="logo">
        <span class="logo__mark"></span>
        <span class="logo__name">TV Surfacing<br>Contractors</span>
      </div>
      <p class="tagline">Concrete Grinding &amp; Polishing<br>Industrial Resin Floors</p>
      <div class="photo cover__photo" role="img" aria-label="Photo of a polished terrazzo-style concrete entry floor beside a grey front door"></div>
      <svg class="cover__dot" width="22" height="22" viewBox="0 0 22 22" aria-hidden="true"><circle cx="11" cy="11" r="11" fill="#e8212b"/></svg>
      <div class="cover__strip cover__strip--bottom"></div>
    </section>
  </main>
</body>
</html>
```